Remote Computer Support PostCard

We need a Postcard Ad for marketing to businesses that need Remote Computer Support and Security. 2 sided and able to be mailed. Can be any color but color we use mostly is red. Remote Computer Support and Security per PC. Includes Remote Monitoring and Maintenance(RMM) Agent, Business Security Tools including Antivirus, Anti Malware, Ransomware Protection, Intrusion Prevention, Content Filtering and others. All remote support you need for $69.99 per pc per month.

Target Market(s)

All Businesses

Industry/Entity Type

Computer Support for Businesses

Colors
EB3D1F
EC4F4E
F09395
F8D3D4
FCEDEE

Requirements
Must have
• Bytharo, Inc. (555) 314-2968 . Sales@bytharo-example.com. Designed to be mailed. 6x9 Postcard Mailer Size Final 6.25" x 9" Ink & Bleed Four Color Process, Full Bleed Two Sides. Must have places for postage.
Nice to have
• Main lines should be in top 1/3 of postcard to stand out in mail.

```html
<!DOCTYPE html>
<html lang="en">
<head>
<meta charset="utf-8">
<title>Bytharo Remote Support Postcard</title>
<link href="https://fonts.googleapis.com/css2?family=Montserrat:wght@300;400;500;700;800&family=Roboto+Condensed:wght@400&display=swap" rel="stylesheet">
<style>
  :root{
    --red:#e1262d;
    --red-dark:#c31d24;
    --navy:#1a2d5c;
    --blue:#1f6fae;
    --blue-light:#2c86c6;
    --ink:#2a2a2a;
    --page:#eceef1;
    --white:#ffffff;
    --rule:#9aa3b5;
  }
  *{box-sizing:border-box;margin:0;padding:0}
  html,body{width:1200px;height:922px;overflow:hidden}
  body{background:var(--page);font-family:"Montserrat",sans-serif;color:var(--ink);position:relative}
  .card{position:absolute;left:290px;width:620px;height:413px;background:var(--white);overflow:hidden;box-shadow:0 6px 18px rgba(0,0,0,.18)}
  .card--front{top:30px}
  .card--back{top:479px}
  .card__art{position:absolute;inset:0;width:620px;height:413px}
  .abs{position:absolute}

  /* front */
  .brand{left:22px;top:24px;display:flex;align-items:center;gap:6px}
  .brand__mark{width:12px;height:12px;background:var(--red)}
  .brand__name{font-weight:700;font-size:21px;color:var(--ink);letter-spacing:-.3px}
  .contact{left:280px;top:28px;width:152px;text-align:right}
  .contact__phone{font-weight:800;font-size:14px;color:var(--red);line-height:1.1}
  .contact__email{font-size:7.5px;color:var(--ink)}
  .headline{left:22px;top:84px;font-weight:800;font-size:26.5px;line-height:1.2;color:var(--white);letter-spacing:.4px}
  .offer{left:22px;top:198px;font-size:16px;color:var(--navy);display:flex;align-items:baseline;gap:10px}
  .offer__price{font-weight:800;font-size:21px;color:var(--red)}
  .tagline{left:30px;top:227px;font-weight:700;font-size:8.2px;color:var(--white);letter-spacing:.1px}
  .section{left:22px;top:250px;width:285px}
  .section__title{font-weight:700;font-size:9.2px;line-height:1.15;color:var(--red)}
  .section__text{font-size:9px;line-height:1.15}
  .section__includes{margin-top:3px;font-weight:700;font-size:9px;line-height:1.15;color:var(--red)}
  .checks{left:22px;top:358px;display:grid;grid-template-columns:255px 180px;row-gap:5px}
  .check{display:flex;gap:5px;font-size:8px;line-height:1.1;text-transform:uppercase}
  .check svg{flex:0 0 9px;width:9px;height:10px}
  .pricetag{left:459px;top:279px;width:126px;text-align:center;color:var(--white)}
  .pricetag__setup{font-weight:700;font-size:7px;line-height:1.15}
  .pricetag__big{font-weight:800;font-size:27px;line-height:1}
  .pricetag__then{font-weight:400;font-size:12.5px;line-height:1.1}
  .pricetag__small{font-size:12.5px;line-height:1.1}
  .pricetag__unit{font-size:6.3px}

  /* back */
  .back-title{left:24px;top:5px;font-weight:700;font-size:13.5px;color:var(--white);letter-spacing:.6px}
  .features{top:32px;display:flex;flex-direction:column;gap:4px}
  .features--left{left:16px;width:196px}
  .features--right{left:213px;width:166px}
  .feature{display:flex;gap:5px}
  .feature svg{flex:0 0 7px;width:7px;height:8px;margin-top:1px}
  .feature__title{font-weight:700;font-size:8px;line-height:1.15;color:var(--red)}
  .feature__text{font-family:"Roboto Condensed",sans-serif;font-size:6.7px;line-height:1.22;color:var(--ink)}
</style>
</head>
<body>

<svg width="0" height="0" style="position:absolute">
  <defs>
    <symbol id="tick" viewBox="0 0 10 11">
      <path d="M5 .6 9.2 2v3.4C9.2 8 7.4 9.6 5 10.4 2.6 9.6.8 8 .8 5.4V2Z" fill="none" stroke="#e1262d" stroke-width="1.2"/>
      <path d="M2.9 5.3 4.5 6.9 7.4 3.7" fill="none" stroke="#e1262d" stroke-width="1.3"/>
    </symbol>
  </defs>
</svg>

<section class="card card--front">
  <svg class="card__art" viewBox="0 0 620 413">
    <defs>
      <linearGradient id="bannerBlue" x1="0" x2="1">
        <stop offset="0" stop-color="#2c86c6"/><stop offset=".6" stop-color="#1f5a98"/><stop offset="1" stop-color="#1a2d5c"/>
      </linearGradient>
      <linearGradient id="footBlue" x1="0" x2="1">
        <stop offset="0" stop-color="#2c86c6"/><stop offset="1" stop-color="#1a2d5c"/>
      </linearGradient>
      <linearGradient id="photoFill" x1="0" y1="0" x2="1" y2="1">
        <stop offset="0" stop-color="#0d3a5e"/><stop offset=".5" stop-color="#1a9ec0"/><stop offset="1" stop-color="#5a4a44"/>
      </linearGradient>
      <linearGradient id="tagFill" x1="0" y1="0" x2="0" y2="1">
        <stop offset="0" stop-color="#2c86c6"/><stop offset="1" stop-color="#1a2d5c"/>
      </linearGradient>
    </defs>
    <polygon points="540,0 620,0 620,215" fill="var(--red)"/>
    <polygon points="600,60 620,48 620,125 600,115" fill="var(--navy)"/>
    <polygon points="0,74 470,74 432,192 0,192" fill="url(#bannerBlue)"/>
    <polygon points="620,190 620,300 560,260" fill="var(--navy)"/>
    <polygon points="430,240 510,140 575,140 492,240" fill="var(--red)"/>
    <polygon points="22,224 592,224 580,240 22,240" fill="var(--red)"/>
    <line x1="318" y1="346" x2="430" y2="346" stroke="var(--rule)" stroke-width=".8"/>
    <line x1="22" y1="349" x2="408" y2="349" stroke="var(--rule)" stroke-width=".6"/>
    <line x1="462" y1="17" x2="483" y2="34" stroke="var(--navy)" stroke-width="1.6"/>
    <line x1="416" y1="17" x2="463" y2="17" stroke="var(--navy)" stroke-width="1.6"/>
    <polygon points="603,135 554.5,219 457.5,219 409,135 457.5,51 554.5,51" fill="var(--navy)"/>
    <polygon points="597,135 551.5,213.8 460.5,213.8 415,135 460.5,56.2 551.5,56.2" fill="var(--white)"/>
    <polygon points="591,135 548.5,208.6 463.5,208.6 421,135 463.5,61.4 548.5,61.4" fill="var(--navy)"/>
    <polygon points="586,135 546,204.3 466,204.3 426,135 466,65.7 546,65.7" fill="url(#photoFill)" role="img" aria-label="Photo of hands on a tablet with a glowing security shield and network icons"/>
    <polygon points="596,337 559,401 485,401 448,337 485,273 559,273" fill="var(--white)" stroke="var(--red)" stroke-width="1.5"/>
    <polygon points="590,337 556,396 488,396 454,337 488,278 556,278" fill="url(#tagFill)"/>
    <rect x="0" y="398" width="620" height="15" fill="url(#footBlue)"/>
  </svg>

  <div class="abs brand"><span class="brand__mark"></span><span class="brand__name">Bytharo</span></div>
  <div class="abs contact">
    <div class="contact__phone">(555) 314-2968</div>
    <div class="contact__email">Sales@bytharo-example.com</div>
  </div>
  <h1 class="abs headline">FINALY, COMPUTER<br>SECURITY AND<br>SUPPORT MADE EASY</h1>
  <div class="abs offer"><span>FOR ONLY</span><span class="offer__price">$69.99</span><span>/ MONTH PER PC</span></div>
  <p class="abs tagline">YOU CAN GET WORLD CLASS SECURITY SERVICES AND UNLIMITEDREMOTE TECHNICAL SUPPORT.</p>
  <div class="abs section">
    <h2 class="section__title">AUTOMATED REMOTE SUPPORT</h2>
    <p class="section__text">Remote monitoring and maintenance tools monitor<br>your devices in real-time. Instantly informing you of current<br>issues and flagging potential problems.</p>
    <h3 class="section__includes">Includes:</h3>
    <p class="section__text">Remote Monitoring and Management Agent (RMM)<br>Help Desk Application on Desktop<br>Kestrova SteadyGuard Business Security</p>
  </div>
  <div class="abs checks">
    <div class="check"><svg><use href="#tick"/></svg><span>Automated Paneo Updates</span></div>
    <div class="check"><svg><use href="#tick"/></svg><span>Automated System Cleanup</span></div>
    <div class="check"><svg><use href="#tick"/></svg><span>Managed Antivirus including ransomware<br>detection and protection</span></div>
    <div class="check"><svg><use href="#tick"/></svg><span>Monthly Reports</span></div>
  </div>
  <div class="abs pricetag">
    <div class="pricetag__setup">ONE TIME SETUP<br>FEE OF</div>
    <div class="pricetag__big">$69.99</div>
    <div class="pricetag__then">THEN ONLY</div>
    <div class="pricetag__small">$69.99</div>
    <div class="pricetag__unit">PER MONTH PER PC</div>
  </div>
</section>

<section class="card card--back">
  <svg class="card__art" viewBox="0 0 620 413">
    <defs>
      <linearGradient id="headBlue" x1="0" x2="1">
        <stop offset="0" stop-color="#1f6fae"/><stop offset="1" stop-color="#1a2d5c"/>
      </linearGradient>
      <linearGradient id="baseBlue" x1="0" x2="1">
        <stop offset="0" stop-color="#2c86c6"/><stop offset="1" stop-color="#1a2d5c"/>
      </linearGradient>
    </defs>
    <polygon points="0,0 315,0 290,25 0,25" fill="url(#headBlue)"/>
    <line x1="390" y1="30" x2="390" y2="385" stroke="var(--rule)" stroke-width="1"/>
    <rect x="529" y="29" width="76" height="104" fill="none" stroke="var(--navy)" stroke-width="1" role="img" aria-label="Postage stamp area"/>
    <g stroke="var(--navy)" stroke-width=".8">
      <line x1="403" y1="255" x2="605" y2="255"/>
      <line x1="403" y1="287" x2="605" y2="287"/>
      <line x1="403" y1="318" x2="605" y2="318"/>
      <line x1="403" y1="350" x2="605" y2="350"/>
    </g>
    <polygon points="0,400 620,400 620,413 0,413" fill="url(#baseBlue)"/>
  </svg>

  <h2 class="abs back-title">ANTIVIRUS</h2>

  <div class="abs features features--left">
    <div class="feature"><svg><use href="#tick"/></svg><div><div class="feature__title">Smart Scan</div><p class="feature__text">Smart Scan leverages anti-malware and antispyware signatures stored in-the-cloud.</p></div></div>
    <div class="feature"><svg><use href="#tick"/></svg><div><div class="feature__title">Real-Time Scan</div><p class="feature__text">Scan a file for security risks when the file is received, opened, downloaded, copied, or modified.</p></div></div>
    <div class="feature"><svg><use href="#tick"/></svg><div><div class="feature__title">Scheduled Scan</div><p class="feature__text">Scan at the configured time and frequency. Use Scheduled Scan to automate routine scans on endpoints and improve the efficiency of threat management.</p></div></div>
    <div class="feature"><svg><use href="#tick"/></svg><div><div class="feature__title">Manual Scan</div><p class="feature__text">An on-demand scan started from the Security Agents screen or the Security Agent console.</p></div></div>
    <div class="feature"><svg><use href="#tick"/></svg><div><div class="feature__title">Behavior Monitoring</div><p class="feature__text">Behavior Monitoring protects endpoints from unauthorized changes to the operating system, registry entries, other software, or files and folders.</p></div></div>
    <div class="feature"><svg><use href="#tick"/></svg><div><div class="feature__title">Malware Behavior Blocking</div><p class="feature__text">Block known and potential threats</p></div></div>
    <div class="feature"><svg><use href="#tick"/></svg><div><div class="feature__title">Ransomware Protection</div><p class="feature__text">Protect documents against unauthorized encryption or modification Automatically back up and restore files changed by suspicious programs Block processes commonly associated with ransomware Enable program inspection to detect and block compromised executable files.</p></div></div>
    <div class="feature"><svg><use href="#tick"/></svg><div><div class="feature__title">Anti-Exploit Protection</div><p class="feature__text">Prevent unauthorized changes to Ledgerly™ files and folders</p></div></div>
    <div class="feature"><svg><use href="#tick"/></svg><div><div class="feature__title">Ledgerly™ Protection</div><p class="feature__text">Terminate programs that exhibit abnormal behavior associated with exploit attacks</p></div></div>
    <div class="feature"><svg><use href="#tick"/></svg><div><div class="feature__title">Event Monitoring</div><p class="feature__text">Monitor system events to filter potentially malicious actions</p></div></div>
    <div class="feature"><svg><use href="#tick"/></svg><div><div class="feature__title">Web Reputation</div><p class="feature__text">Web Reputation enhances protection against malicious websites.</p></div></div>
    <div class="feature"><svg><use href="#tick"/></svg><div><div class="feature__title">Predictive Machine Learning</div><p class="feature__text">Kestrova Predictive Machine Learning uses advanced machine learning technology to detect emerging unknown security risks found in low-prevalence suspicious processes or files.</p></div></div>
  </div>

  <div class="abs features features--right">
    <div class="feature"><svg><use href="#tick"/></svg><div><div class="feature__title">Vulnerability Protection</div><p class="feature__text">SteadyGuard Services now provides Intrusion Prevention Rules to protect your endpoints. Vulnerability Protection uses a host-based intrusion prevention system (HIPS) to apply virtual patches to known vulnerabilities. This feature is part of the comprehensive protection thatincludes Behavior Monitoring, Firewall, and PredictiveMachine Learning.</p></div></div>
    <div class="feature"><svg><use href="#tick"/></svg><div><div class="feature__title">Browser Exploit Prevention</div><p class="feature__text">Block websites containing malicious script</p></div></div>
    <div class="feature"><svg><use href="#tick"/></svg><div><div class="feature__title">Firewall</div><p class="feature__text">The firewall can block or allow certain types of network traffic by creating a barrier between the endpoint and the network.</p></div></div>
    <div class="feature"><svg><use href="#tick"/></svg><div><div class="feature__title">Device Control</div><p class="feature__text">Device Control regulates access to peripheral devices.</p></div></div>
    <div class="feature"><svg><use href="#tick"/></svg><div><div class="feature__title">Data Loss Prevention</div><p class="feature__text">Data Loss Prevention monitors or blocks sensitive data transmissions across your network.</p></div></div>
    <div class="feature"><svg><use href="#tick"/></svg><div><div class="feature__title">URL Filtering</div><p class="feature__text">URL Filtering allows administrators to block specific types of websites during different times of the day.</p></div></div>
    <div class="feature"><svg><use href="#tick"/></svg><div><div class="feature__title">Application Control</div><p class="feature__text">Create rules to restrict the applications that can execute or install on the endpoints.</p></div></div>
  </div>
</section>

</body>
</html>
```